Certificate of Completion - Educational Trainings

We are looking for a certificate of completion for individuals who complete one of our specific trainings. Files should be provided in a Word (docx) or PowerPoint (pptx) format. The "Talmoray example.png" file is to show necessary information. Copies of logos have been included for design purposes.

Target Market(s)

Training Participants

Industry/Entity Type

Healthcare

Font styles to use
Sans Serif

```html
<!DOCTYPE html>
<html lang="en">
<head>
<meta charset="utf-8">
<title>Talmoray Certificate of Completion</title>
<link rel="stylesheet" href="https://fonts.googleapis.com/css2?family=Montserrat:wght@800&family=Poppins:wght@300;400;500;600&family=Cormorant+Garamond:ital,wght@1,500&display=swap">
<style>
  :root {
    --stage: #232323;
    --forest: #3b6331;
    --leaf: #8db55e;
    --paper: #ffffff;
    --ink: #111111;
    --muted: #6b6b6b;
  }
  html, body { margin: 0; padding: 0; overflow: hidden; }
  body { width: 1200px; height: 1200px; background: var(--stage); position: relative; font-family: "Poppins", sans-serif; }
  .certificate { position: absolute; left: 169px; top: 294px; width: 861px; height: 611px; background: var(--forest); }
  .certificate__frame { position: absolute; left: 0; top: 0; }
  .abs { position: absolute; left: 0; width: 100%; text-align: center; margin: 0; }
  .brand { top: 68px; font-family: "Montserrat", sans-serif; font-weight: 800; font-size: 30px; letter-spacing: 2px; color: var(--ink); }
  .brand__mark { display: inline-block; width: 22px; height: 22px; border-radius: 50%; background: var(--forest); vertical-align: -2px; margin-right: 12px; }
  .address { top: 117px; font-size: 10.5px; line-height: 13.5px; color: var(--ink); text-transform: uppercase; letter-spacing: -0.2px; }
  .rule { position: absolute; height: 1px; background: var(--forest); }
  .rule--short { left: 379px; top: 172px; width: 106px; }
  .title { top: 166px; font-weight: 300; font-size: 79px; line-height: 104px; color: var(--ink); letter-spacing: 1px; }
  .subtitle { top: 256px; font-family: "Cormorant Garamond", serif; font-style: italic; font-weight: 500; font-size: 32px; color: var(--ink); }
  .awarded { top: 303px; font-size: 10.5px; color: var(--ink); text-transform: uppercase; letter-spacing: -0.2px; }
  .rule--name { left: 191px; top: 360px; width: 484px; height: 2px; }
  .details { top: 369px; font-size: 11.5px; line-height: 16.8px; color: var(--muted); letter-spacing: 1px; font-weight: 500; }
  .signature { position: absolute; top: 493px; border-top: 2px solid var(--forest); padding-top: 3px; font-size: 10px; letter-spacing: 2px; color: #333; text-transform: uppercase; }
  .signature--date { left: 141px; width: 148px; text-align: center; }
  .signature--consultant { left: 589px; width: 143px; text-align: center; }
  .seal { position: absolute; left: 391px; top: 466px; width: 68px; height: 68px; border-radius: 50%; background: var(--leaf); }
  .footnote { top: 549px; font-size: 7px; font-weight: 600; letter-spacing: 1px; color: #333; text-transform: uppercase; }
</style>
</head>
<body>
  <main class="certificate">
    <svg class="certificate__frame" width="861" height="611" viewBox="0 0 861 611" aria-hidden="true">
      <path d="M62 29 L807 29 A24 24 0 0 0 831 53 L831 558 A24 24 0 0 0 807 582 L62 582 A24 24 0 0 0 38 558 L38 53 A24 24 0 0 0 62 29 Z" fill="var(--leaf)"/>
      <path d="M66 34 L803 34 A22 22 0 0 0 825 56 L825 555 A22 22 0 0 0 803 577 L66 577 A22 22 0 0 0 44 555 L44 56 A22 22 0 0 0 66 34 Z" fill="var(--paper)"/>
      <path d="M72 41 L797 41 A20 20 0 0 0 817 61 L817 550 A20 20 0 0 0 797 570 L72 570 A20 20 0 0 0 52 550 L52 61 A20 20 0 0 0 72 41 Z" fill="none" stroke="var(--leaf)" stroke-width="1.5"/>
    </svg>

    <p class="abs brand"><span class="brand__mark"></span>TALMORAY</p>
    <p class="abs address">48 Harbor Lane, Ste. 310<br>Brookfield, ME 04210<br>National Registry Sponsor Number 58213</p>
    <div class="rule rule--short"></div>

    <h1 class="abs title">CERTIFICATE</h1>
    <p class="abs subtitle">of completion</p>
    <p class="abs awarded">This certificate is awarded to</p>
    <div class="rule rule--name"></div>

    <p class="abs details">For successful completion of<br>Best Practices: Budget Process/Budget Building<br>Completed Online<br>Field of Study Finance<br>CPE Credits: 1</p>

    <div class="signature signature--date">Completion Date</div>
    <div class="seal"></div>
    <div class="signature signature--consultant">Senior Consultant</div>

    <p class="abs footnote">In accordance with the standard of the national registry of CPE sponsors, CPE credits have been granted based on a 50 minute hour.</p>
  </main>
</body>
</html>
```